livestock sales postcard schedule

Livestock marketing company fall 2015 sales scheduleReturn address on mailing side: CEDARHOLLOW RIDGE CATTLE MART PO BOX 482 ASHVALE, WEST VIRGINIA 26836Would like pale blue background if it works
Updates

My mistake: the phone number for Dale is 555-418-0187

Target Market(s)

Livestock sellers in area and buyers

Industry/Entity Type

It Company

Font styles to use
Sans Serif

Requirements
Must have
• Picture and text enclosed
Nice to have
• "Feeder sales on CALL-N-Bidder" somewhere
• Auction hammer under return address in area

```html
<!DOCTYPE html>
<html lang="en">
<head>
<meta charset="utf-8">
<title>Fall Sale Schedule 2015 Postcard</title>
<link href="https://fonts.googleapis.com/css2?family=Oswald:wght@400;500;600&family=Open+Sans:wght@400;600&display=swap" rel="stylesheet">
<style>
  :root {
    --page: #e6e8ea;
    --card: #ffffff;
    --brown: #8a5634;
    --brown-soft: #c9a586;
    --grey-text: #6f6a66;
    --band: #9a948f;
    --band-dark: #7c7671;
    --navy: #2d4657;
    --line: #b9b4b0;
  }
  * { box-sizing: border-box; margin: 0; padding: 0; }
  html, body { width: 900px; height: 1200px; overflow: hidden; }
  body {
    background: var(--page);
    font-family: "Open Sans", sans-serif;
    position: relative;
  }
  .postcard {
    position: absolute;
    left: 40px;
    width: 820px;
    height: 565px;
    background: var(--card);
    box-shadow: 0 4px 14px rgba(0,0,0,0.18);
    overflow: hidden;
  }
  .postcard--front { top: 25px; }
  .postcard--back { top: 610px; }

  /* Front */
  .front-photo {
    position: absolute; inset: 0 0 auto 0; height: 470px;
    background:
      radial-gradient(ellipse 45% 40% at 55% 45%, #9c9894 0%, #8a8681 45%, transparent 75%),
      linear-gradient(135deg, #c7b39a 0%, #a88c6d 35%, #d8d2c8 60%, #b9986e 100%);
  }
  .front-swoosh { position: absolute; left: 0; top: 360px; width: 820px; height: 140px; }
  .front-caption {
    position: absolute; left: 0; right: 0; top: 488px;
    text-align: center;
    font-family: "Oswald", sans-serif; font-weight: 600;
    font-size: 30px; letter-spacing: 0.5px;
    color: var(--brown);
  }

  /* Back */
  .back-deco { position: absolute; left: 0; top: 0; width: 820px; height: 60px; }
  .schedule-band {
    position: absolute; left: 0; top: 58px; width: 360px; height: 50px;
    background: linear-gradient(90deg, var(--band-dark), var(--band) 70%, #c3beba);
    display: flex; align-items: center; padding-left: 20px;
    font-family: "Oswald", sans-serif; font-weight: 600;
    font-size: 25px; color: #fff; letter-spacing: 0.5px;
  }
  .schedule-list {
    position: absolute; left: 20px; top: 124px;
    list-style: none;
    font-family: "Oswald", sans-serif; font-weight: 400;
    font-size: 15.5px; line-height: 20.5px; color: var(--grey-text);
  }
  .back-photo {
    position: absolute; left: 18px; top: 430px; width: 230px; height: 115px;
    border-radius: 18px; border: 4px solid var(--brown-soft);
    background:
      radial-gradient(ellipse 40% 45% at 55% 50%, #9a9692 0%, transparent 75%),
      linear-gradient(135deg, #c7b39a, #a88c6d 40%, #d5cec4 70%, #b9986e);
  }
  .divider {
    position: absolute; left: 420px; top: 150px; width: 1px; height: 370px;
    background: var(--line);
  }
  .stamp-box {
    position: absolute; left: 648px; top: 70px; width: 130px; height: 125px;
    border: 2px solid #8d8782;
  }
  .address-line {
    position: absolute; left: 470px; width: 310px; height: 1px; background: var(--line);
  }
  .return-address {
    position: absolute; left: 470px; top: 448px; width: 310px;
    text-align: center;
    font-family: "Oswald", sans-serif; font-weight: 500; font-style: normal;
    font-size: 17px; line-height: 21px; color: var(--navy);
    text-transform: uppercase;
  }
</style>
</head>
<body>

<section class="postcard postcard--front">
  <div class="front-photo" role="img" aria-label="Photograph of a grey cat lounging on papers on a desk"></div>
  <svg class="front-swoosh" viewBox="0 0 820 140" preserveAspectRatio="none" aria-hidden="true">
    <path d="M0 40 Q410 150 820 20 L820 140 L0 140 Z" fill="#ffffff"/>
    <path d="M0 40 Q410 150 820 20 L820 38 Q410 165 0 60 Z" fill="var(--brown)"/>
    <path d="M0 66 Q410 168 820 44 L820 52 Q410 176 0 74 Z" fill="var(--brown-soft)"/>
  </svg>
  <p class="front-caption">BISCUIT THINKS CEDARHOLLOW IS THE CAT'S MEOOOW!!!</p>
</section>

<section class="postcard postcard--back">
  <svg class="back-deco" viewBox="0 0 820 60" preserveAspectRatio="none" aria-hidden="true">
    <path d="M0 0 L820 0 L820 18 Q420 70 0 30 Z" fill="#ece4dc"/>
    <path d="M0 30 Q420 70 820 18 L820 24 Q420 78 0 36 Z" fill="var(--brown-soft)"/>
  </svg>
  <h2 class="schedule-band">FALL SALE SCHEDULE 2015</h2>
  <ul class="schedule-list">
    <li>SAT. SEPT 19 - 10:00 AM</li>
    <li>SAT. OCT 3 - 10:00 AM</li>
    <li>SAT. OCT 10 - 10:00 AM</li>
    <li>SAT. OCT 17 - 10:00 AM</li>
    <li>SAT. OCT 24 - 10:00 AM</li>
    <li>SAT. NOV 7 - 10:00 AM</li>
    <li>FEEDER TAKE-IN, FRI 7 - 5</li>
    <li>SALE EVERY WEDNESDAY</li>
    <li>COW SALE FRI. OCT 30</li>
    <li>BARN 555-226-0953</li>
    <li>WADE 555-302-7741</li>
    <li>DALE 555-418-0187</li>
  </ul>
  <div class="back-photo" role="img" aria-label="Small photograph of the grey cat"></div>

  <div class="divider"></div>
  <div class="stamp-box"></div>
  <div class="address-line" style="top:250px"></div>
  <div class="address-line" style="top:300px"></div>
  <div class="address-line" style="top:350px"></div>
  <div class="address-line" style="top:400px"></div>

  <address class="return-address">
    Cedarhollow Ridge<br>
    Cattle Mart<br>
    PO Box 482 Ashvale,<br>
    West Virginia 25914
  </address>
</section>

</body>
</html>
```